Kestrel Arc Services business card Design

I need a business card that will wow clients at first sight.

Kestrel Arc Services connects people with HOME & LIFESTYLE SERVICES, and the client pays the value that was created by our service, using. 'Pay What You Think It's Worth".
Please look us up at www.kestrelarcservices.com to see our mission and services.

The new website is being launched in 8 weeks.

I need a business card to campaign LANDSCAPING however please design it to be easily modified to CLEANING SERVICE, PLUMBING Etc Etc.

Until our SEO campaign begins working I need business cards to leave with prospective clients for each individual service as appropriate.

Orla Pemberton
Creative Director
www.kestrelarcservices.com
1-888-617-4KAS
email: info@kestrelarcservices.com

Target Market(s)

Residential and commercial clients

Industry/Entity Type

Business

Contact Information for Business Card

2 sided

Font styles to use
Sans Serif

Requirements
Must have
• Im prefering a black card so far
• Logo
• "Pay what You Think It's Worth" seal
• Complete Landscaping & Construction
• Trundler Services
• Contact details
• facebook kestrelarc services
• twitter @kestrelarc services
• Adaptable card easily to different services we offer at Kestrel Arc Services as per www.kestrelarcservices.com
Should not have
• Too much imagery

```html
<!DOCTYPE html>
<html lang="en">
<head>
<meta charset="utf-8">
<title>Kestrel Arc Services – Business Card</title>
<link rel="stylesheet" href="https://fonts.googleapis.com/css2?family=Open+Sans:wght@400;600&display=swap">
<style>
  :root {
    --backdrop: #5b3e2b;
    --card: #262626;
    --logo-grey: #b4b4b4;
    --tag-grey: #9a9a9a;
    --text-light: #c9c9c9;
    --green: #7dc04e;
    --teal: #2a8fa3;
    --blue: #3d63b8;
    --purple: #7b4fb2;
    --gold: #c9a23a;
    --navy: #1d2360;
  }
  * { box-sizing: border-box; margin: 0; padding: 0; }
  html, body { width: 1200px; height: 1000px; overflow: hidden; }
  body {
    position: relative;
    background: var(--backdrop);
    font-family: "Open Sans", Arial, sans-serif;
  }
  .card {
    position: absolute;
    left: 265px;
    width: 665px;
    height: 397px;
    background: var(--card);
    overflow: hidden;
    box-shadow: 0 6px 14px rgba(0,0,0,.45);
  }
  .card--front { top: 73px; }
  .card--back { top: 533px; }

  .brand { position: absolute; }
  .brand__row { display: flex; align-items: center; gap: 12px; }
  .brand__dot { width: 30px; height: 30px; border-radius: 50%; background: var(--blue); flex: none; }
  .brand__name { font-size: 27px; font-weight: 400; color: var(--logo-grey); white-space: nowrap; line-height: 1; }
  .brand__tagline {
    margin: 8px 0 0 42px;
    font-size: 10px; letter-spacing: 5px; color: var(--tag-grey); white-space: nowrap;
  }
  .card--front .brand { left: 32px; top: 66px; }
  .card--back .brand { left: 120px; top: 168px; z-index: 1; }

  .person { position: absolute; left: 121px; top: 162px; }
  .person__name { font-size: 20px; font-weight: 600; color: var(--green); line-height: 1.2; }
  .person__title { font-size: 16px; color: var(--text-light); margin-top: 2px; }

  .contacts { position: absolute; left: 121px; top: 223px; list-style: none; }
  .contacts li { display: flex; align-items: center; gap: 8px; font-size: 16px; color: var(--text-light); height: 24.5px; }
  .contacts svg { width: 16px; height: 16px; fill: var(--green); flex: none; }

  .social { position: absolute; left: 121px; top: 303px; list-style: none; }
  .social li { display: flex; align-items: center; gap: 6px; font-size: 16px; color: var(--text-light); height: 25px; }
  .social__my { color: var(--green); }
  .social__mark { width: 15px; height: 15px; border-radius: 50%; background: var(--green); }

  .seal {
    position: absolute; left: 372px; top: 222px; width: 90px; height: 90px; border-radius: 50%;
    background: var(--navy); border: 6px solid var(--gold);
  }

  .services { position: absolute; right: 0; top: 0; width: 200px; height: 100%; list-style: none; }
  .service { position: absolute; right: 0; display: flex; align-items: center; gap: 18px; }
  .service__label { font-size: 16px; text-align: right; line-height: 1.25; }
  .service__tab { width: 17px; height: 32px; border-radius: 16px 0 0 16px; }
  .service--landscape { top: 47px; } .service--landscape .service__label { color: var(--green); } .service--landscape .service__tab { background: var(--green); }
  .service--trundler { top: 123px; } .service--trundler .service__label { color: var(--teal); } .service--trundler .service__tab { background: var(--teal); }
  .service--cleaning { top: 191px; } .service--cleaning .service__label { color: var(--blue); } .service--cleaning .service__tab { background: var(--blue); }
  .service--plumbing { top: 260px; } .service--plumbing .service__label { color: var(--purple); } .service--plumbing .service__tab { background: var(--purple); }
  .service--remodel { top: 327px; } .service--remodel .service__label { color: var(--teal); } .service--remodel .service__tab { background: var(--teal); }

  .backdrop-motif {
    position: absolute; left: 285px; top: 5px; width: 380px; height: 370px;
    background: radial-gradient(ellipse at center, #1e1e1e 0%, rgba(30,30,30,.6) 50%, rgba(38,38,38,0) 75%);
  }
  .back-url {
    position: absolute; left: 0; right: 0; top: 347px; text-align: center;
    font-size: 16px; letter-spacing: 1.3px; color: var(--text-light);
  }
</style>
</head>
<body>

<section class="card card--front">
  <div class="brand">
    <div class="brand__row"><span class="brand__dot"></span><span class="brand__name">Kestrel Arc Services Inc.</span></div>
    <p class="brand__tagline">HONEST WORK, FAIR VALUE</p>
  </div>

  <div class="person">
    <p class="person__name">Orla Pemberton</p>
    <p class="person__title">Creative Director</p>
  </div>

  <ul class="contacts">
    <li><svg viewBox="0 0 16 16"><path d="M2 5c0-2 2-3 6-3s6 1 6 3v1h-3V5H5v1H2zM4 8h8l2 6H2z"/></svg>1-888-617-4KAS</li>
    <li><svg viewBox="0 0 16 16"><path d="M1 3h14v10H1zM2.5 4.5 8 9l5.5-4.5v-.2h-11z" fill-rule="evenodd"/></svg>info@kestrelarcservices.com</li>
    <li><svg viewBox="0 0 16 16"><path d="M8 1a7 7 0 1 0 0 14A7 7 0 0 0 8 1zm0 2a5 5 0 0 1 0 10A5 5 0 0 1 8 3z"/><path d="M7 6l7 3-3 1-1 3z"/></svg>www.kestrelarcservices.com</li>
  </ul>

  <ul class="social">
    <li><span class="social__my">My</span><span class="social__mark"></span>kestrelarc services</li>
    <li><span class="social__my">My</span><span class="social__mark"></span>@kestrelarc services</li>
  </ul>

  <div class="seal" role="img" aria-label="Round gold-rimmed pricing seal"></div>

  <ul class="services">
    <li class="service service--landscape"><span class="service__label">Landscaping<br>Construction</span><span class="service__tab"></span></li>
    <li class="service service--trundler"><span class="service__label">Trundler</span><span class="service__tab"></span></li>
    <li class="service service--cleaning"><span class="service__label">Cleaning</span><span class="service__tab"></span></li>
    <li class="service service--plumbing"><span class="service__label">Plumbing</span><span class="service__tab"></span></li>
    <li class="service service--remodel"><span class="service__label">Remodeling</span><span class="service__tab"></span></li>
  </ul>
</section>

<section class="card card--back">
  <div class="backdrop-motif" role="img" aria-label="Faint dark circle pattern"></div>
  <div class="brand">
    <div class="brand__row"><span class="brand__dot"></span><span class="brand__name">Kestrel Arc Services Inc.</span></div>
    <p class="brand__tagline">HONEST WORK, FAIR VALUE</p>
  </div>
  <p class="back-url">www.kestrelarcservices.com</p>
</section>

</body>
</html>
```